Career Counselor in need of a business card design

Hello Creatives! I'm in need of a business card design for a new company based in Georgia, USA called Pathways By Lumen.

Some things that may be helpful in creating your concept(s) include:

My Logo (Included in the Files section): There are three versions, two versions are in the second file. The all gold stacked (vertical) version is my primary logo and then there are two horizontal versions (one is all gold and the other is gold and grey).

My mission: to empower tweens through young adults to realize and actualize their CAREER ASPIRATIONS.
My vision: for tweens through young adults to LIVE LIFE ON PURPOSE and become CONTRIBUTING MEMBERS OF SOCIETY.

Biblical scriptures that support my ‘Why’: Psalms 127: 3-4(NIV) Children are a heritage from the Lord, offspring a reward from him. Like ARROWS in the hands of a warrior are children…. And Proverbs 29:18(JKV) Where there is no VISION, the people perish.

*Words in ALL CAPS are to emphasize what's important to me and may possibly provide you some inspiration (IDK - Have fun with it)!

Target Market(s)

My ideal customers are parents, guardians, and young adults.

Contact Information for Business Card

My name, degrees and credential: Delmira Fosket, M.S., Ed.S., NCC
Title: College and Career Coach and Consultant

Number: 555.317.8842
Address: 2618 Velbrook Avenue., Suite 407, Macon, GA 31299
Email: info@pathwaysbylumen.co
Website: www.pathwaysbylumen.co

My population: TWEENS • TEENS • EMERGING ADULTS
Services offered: One-On-One Sessions • Small Groups • Workshops

Colors

Designer to choose colors to be used in the design.

Requirements
Nice to have
• Either my mission or vision but I will understand if it does not all fit.
• My mission: To empower tweens through young adults to realize and actualize their career aspirations.
• My vision: For tweens through young adults to live life on purpose and become contributing members of society.

```html
<!DOCTYPE html>
<html lang="en">
<head>
<meta charset="UTF-8">
<title>Pathways By Lumen — Business Card</title>
<link rel="stylesheet" href="https://fonts.googleapis.com/css2?family=Cinzel:wght@600&family=Lato:wght@400;700&display=swap">
<style>
  :root {
    --stage: #1c1c1e;
    --card: #0f0f10;
    --card-edge: #1f1f21;
    --gold: #dcb845;
    --silver: #c9c9cc;
    --text-light: #e4e4e4;
    --text-muted: #9c9c9c;
    --rule: #3a3a3c;
  }
  * { box-sizing: border-box; margin: 0; padding: 0; }
  html, body {
    width: 1200px; height: 900px; overflow: hidden;
    background: var(--stage);
    font-family: "Lato", Arial, sans-serif;
  }
  .stage { position: relative; width: 1200px; height: 900px; }
  .card {
    position: absolute; left: 270px;
    width: 660px; height: 378px;
    background: linear-gradient(160deg, #161618 0%, var(--card) 60%);
    border: 1px solid var(--card-edge);
    border-radius: 22px;
    box-shadow: 0 18px 40px rgba(0,0,0,.55);
    overflow: hidden;
  }
  .card--back { top: 50px; }
  .card--front { top: 472px; }

  /* back */
  .back-mark {
    position: absolute; left: 0; right: 0; top: 104px;
    display: flex; flex-direction: column; align-items: center; gap: 16px;
  }
  .mark-dot {
    width: 62px; height: 62px; border-radius: 50%;
    background: var(--silver);
  }
  .back-mark .brand-name {
    font-family: "Cinzel", Georgia, serif; font-weight: 600;
    font-size: 28px; letter-spacing: 2px; color: var(--silver);
  }
  .services {
    position: absolute; left: 0; right: 0; bottom: 56px;
    text-align: center; color: var(--text-light);
    font-size: 15px; letter-spacing: .5px;
  }

  /* front */
  .brand {
    position: absolute; right: 40px; top: 40px;
    display: flex; flex-direction: column; align-items: flex-end; gap: 10px;
  }
  .brand-row { display: flex; align-items: center; gap: 14px; }
  .brand-dot {
    width: 50px; height: 50px; border-radius: 50%; background: var(--gold);
  }
  .brand-row .brand-name {
    font-family: "Cinzel", Georgia, serif; font-weight: 600;
    font-size: 30px; letter-spacing: 1.5px; color: var(--gold);
  }
  .population {
    font-size: 14px; color: var(--text-light); letter-spacing: .5px;
  }
  .rule {
    position: absolute; right: 40px; top: 148px;
    width: 300px; height: 1px; background: var(--rule);
  }
  .address {
    position: absolute; right: 40px; top: 160px;
    text-align: right; color: var(--text-muted);
    font-size: 16px; line-height: 1.4;
  }
  .person {
    position: absolute; left: 44px; top: 222px;
  }
  .person-name {
    font-family: "Cinzel", Georgia, serif; font-weight: 600;
    font-size: 22px; line-height: 1.2; color: var(--gold); letter-spacing: .5px;
  }
  .person-title {
    font-size: 16px; color: var(--text-muted); margin-top: 2px;
  }
  .contact {
    list-style: none; margin-top: 10px;
    display: flex; flex-direction: column; gap: 4px;
  }
  .contact li {
    display: flex; align-items: center; gap: 10px;
    font-size: 16px; line-height: 1.3; color: var(--text-light);
  }
  .contact svg { width: 14px; height: 14px; flex: none; }
</style>
</head>
<body>
<main class="stage">

  <section class="card card--back" aria-label="Business card back">
    <div class="back-mark">
      <span class="mark-dot"></span>
      <span class="brand-name">PATHWAYS BY LUMEN</span>
    </div>
    <p class="services">ONE-ON-ONE SESSIONS • SMALL GROUPS • WORKSHOPS</p>
  </section>

  <section class="card card--front" aria-label="Business card front">
    <div class="brand">
      <div class="brand-row">
        <span class="brand-dot"></span>
        <span class="brand-name">PATHWAYS BY LUMEN</span>
      </div>
      <p class="population">TWEENS • TEENS • EMERGING ADULTS</p>
    </div>
    <div class="rule"></div>
    <p class="address">2618 Velbrook Avenue<br>Suite 407, Macon, GA 31299</p>

    <div class="person">
      <h1 class="person-name">DELMIRA FOSKET, M.S., ED.S., NCC</h1>
      <p class="person-title">College and Career Coach and Consultant</p>
      <ul class="contact">
        <li>
          <svg viewBox="0 0 14 14" aria-hidden="true"><path fill="#dcb845" d="M3 1h2l1 3-1.5 1a7 7 0 0 0 4.5 4.5L10 8l3 1v2a2 2 0 0 1-2 2A10 10 0 0 1 1 3a2 2 0 0 1 2-2z"/></svg>
          555.317.8842
        </li>
        <li>
          <svg viewBox="0 0 14 14" aria-hidden="true"><rect x="1" y="3" width="12" height="8" fill="#dcb845"/><path d="M1 3l6 4.5L13 3" fill="none" stroke="#0f0f10" stroke-width="1.2"/></svg>
          info@pathwaysbylumen.co
        </li>
        <li>
          <svg viewBox="0 0 14 14" aria-hidden="true"><circle cx="7" cy="7" r="6" fill="#dcb845"/><path d="M1 7h12M7 1c-3 3-3 9 0 12M7 1c3 3 3 9 0 12" fill="none" stroke="#0f0f10" stroke-width="1"/></svg>
          www.pathwaysbylumen.co
        </li>
      </ul>
    </div>
  </section>

</main>
</body>
</html>
```